Content marketing firm needs a creative out of the box stationary design

Please take a look to the uploaded logo
I need the whole stationary package which include designs for (business card, letterhead, folder, notepad, company profile, small and big envelop, CD and its cover, key medal, header cover for social media pages "plimbook, chirvel, workloop, pictaro, zorbix+" and website, favicon for website, E-mail signature, flyer, brochure)

```html
<!DOCTYPE html>
<html lang="en">
<head>
<meta charset="utf-8">
<title>Brightvault Media — Business Card</title>
<link rel="stylesheet" href="https://fonts.googleapis.com/css2?family=Damion&family=Josefin+Sans:wght@300;400&family=Nunito:wght@800&display=swap">
<style>
  :root {
    --backdrop-top: #f4f4f4;
    --backdrop-bottom: #dcdddf;
    --card-white: #ffffff;
    --beam-blue: #5fb3e6;
    --beam-light: #94c9ef;
    --ink: #111111;
    --mark-grey: #3b3b3b;
  }
  * { margin: 0; padding: 0; box-sizing: border-box; }
  html, body {
    width: 1200px;
    height: 930px;
    overflow: hidden;
  }
  body {
    background: linear-gradient(180deg, var(--backdrop-top), var(--backdrop-bottom));
    display: flex;
    align-items: center;
    justify-content: center;
  }
  .business-card {
    position: relative;
    width: 330px;
    height: 592px;
    border-radius: 26px;
    background: var(--card-white);
    overflow: hidden;
    box-shadow: 0 10px 30px rgba(0, 0, 0, 0.12);
  }
  .spotlight {
    position: absolute;
    inset: 0;
    width: 100%;
    height: 100%;
  }
  .spotlight .beam-outer { fill: var(--beam-light); }
  .spotlight .beam-core { fill: var(--beam-blue); }
  .contact {
    position: absolute;
    top: 52px;
    left: 0;
    right: 0;
    text-align: center;
    color: var(--card-white);
  }
  .contact-name {
    font-family: "Damion", cursive;
    font-size: 44px;
    font-weight: 400;
    line-height: 1;
    transform: rotate(-4deg);
  }
  .contact-title {
    margin-top: 10px;
    font-family: "Josefin Sans", sans-serif;
    font-weight: 400;
    font-size: 16px;
    letter-spacing: 3px;
    color: var(--ink);
  }
  .contact-phone {
    margin-top: 18px;
    font-family: "Josefin Sans", sans-serif;
    font-weight: 300;
    font-size: 30px;
    letter-spacing: 0.5px;
  }
  .contact-phone .sep { color: var(--ink); font-weight: 400; }
  .brand {
    position: absolute;
    top: 370px;
    left: 0;
    right: 0;
    display: flex;
    flex-direction: column;
    align-items: center;
  }
  .brand-square {
    width: 86px;
    height: 86px;
    background: var(--mark-grey);
  }
  .brand-name {
    margin-top: 18px;
    font-family: "Nunito", sans-serif;
    font-weight: 800;
    font-size: 30px;
    line-height: 1.05;
    letter-spacing: 0.5px;
    color: var(--ink);
    text-align: center;
  }
</style>
</head>
<body>
  <article class="business-card">
    <svg class="spotlight" viewBox="0 0 330 592" preserveAspectRatio="none" aria-hidden="true">
      <polygon class="beam-outer" points="0,0 330,0 330,185 226,372 104,372 0,185"/>
      <polygon class="beam-core" points="0,0 330,0 330,57 226,372 104,372 0,57"/>
    </svg>

    <div class="contact">
      <p class="contact-name">Your Name</p>
      <p class="contact-title">&lt;TITLE&gt;</p>
      <p class="contact-phone"><span class="sep">+</span>1<span class="sep">.</span>000<span class="sep">.</span>000<span class="sep">.</span>0000</p>
    </div>

    <div class="brand">
      <div class="brand-square"></div>
      <p class="brand-name">BRIGHTVAULT<br>MEDIA</p>
    </div>
  </article>
</body>
</html>
```